We need a design for our security installation based business. Our name is K M Security Systems

We need a business card for a security installation based company. We want to look modern and professional. We would like our company logo used and the three main colours to be white, black and orange. We install intruder alarms, cctv and access control. Our preference would be to use the black/orange design on the front and orange/black on the back. Feel free to post variations.

Target Market(s)

Business owners, commercial property and large residential properties

Industry/Entity Type

Business

Contact Information for Business Card

Owen Pellworth 07812 904 226

Liam Foxcombe 07755 618 042

operations@kmsecuritysystems.example.co.uk

Intruder Alarms
CCTV
Access Control

Colors
f78f20
000000
ffffff

Requirements
Must have
• Must have the logo on the business card somewhere

```html
<!DOCTYPE html>
<html lang="en">
<head>
<meta charset="utf-8">
<title>K M Security Systems – Business Card</title>
<link rel="stylesheet" href="https://fonts.googleapis.com/css2?family=Roboto+Condensed:wght@700&family=Roboto:wght@400&display=swap">
<style>
  :root {
    --stage: #2e2a27;
    --card: #1c1d1f;
    --orange: #f78f20;
    --orange-deep: #f2581e;
    --white: #ffffff;
    --silver: #d9dadb;
    --muted: #e6e6e6;
  }
  * { box-sizing: border-box; margin: 0; padding: 0; }
  html, body { width: 1200px; height: 769px; overflow: hidden; }
  body {
    background: var(--stage);
    position: relative;
    font-family: "Roboto", Arial, sans-serif;
  }
  .card {
    position: absolute;
    top: 216px;
    width: 520px;
    height: 336px;
    background: var(--card);
    border-radius: 3px;
    box-shadow: 0 10px 30px rgba(0,0,0,.45);
    overflow: hidden;
  }
  .card--front { left: 50px; }
  .card--back { left: 630px; }

  .brand {
    position: absolute;
    display: flex;
    flex-direction: column;
    align-items: center;
    gap: 10px;
    font-family: "Roboto Condensed", "Arial Narrow", sans-serif;
    font-weight: 700;
    text-transform: uppercase;
    text-align: center;
  }
  .brand__mark { width: 40px; height: 40px; flex: none; }
  .brand__name { font-size: 28px; line-height: 1.05; letter-spacing: 1px; }

  .card--front .brand { left: 30px; width: 230px; top: 118px; color: var(--orange-deep); }
  .card--front .brand__mark { background: var(--orange-deep); }

  .contacts {
    position: absolute;
    left: 278px;
    top: 92px;
    width: 232px;
    color: var(--muted);
  }
  .person { margin-bottom: 12px; }
  .person__name {
    font-family: "Roboto Condensed", "Arial Narrow", sans-serif;
    font-weight: 700;
    font-size: 21px;
    color: var(--orange-deep);
    text-transform: uppercase;
    line-height: 1.05;
  }
  .person__phone { font-size: 15px; letter-spacing: .5px; }
  .links { list-style: none; margin-top: 6px; }
  .links li {
    display: flex; align-items: center; gap: 6px;
    font-size: 10.5px; line-height: 1.6; white-space: nowrap;
  }
  .links svg { width: 10px; height: 10px; flex: none; }

  .card--back .brand {
    left: 0; right: 0; top: 92px;
    color: var(--silver);
  }
  .card--back .brand__mark { background: var(--silver); }
  .services {
    position: absolute;
    left: 0; right: 0; top: 232px;
    text-align: center;
    color: var(--white);
    font-size: 14px;
  }
  .services .dot { color: var(--orange-deep); margin: 0 5px; }
</style>
</head>
<body>
  <section class="card card--front" aria-label="Card front">
    <div class="brand">
      <span class="brand__mark"></span>
      <span class="brand__name">K M Security<br>Systems</span>
    </div>
    <div class="contacts">
      <div class="person">
        <p class="person__name">Owen Pellworth</p>
        <p class="person__phone">07812 904 226</p>
      </div>
      <div class="person">
        <p class="person__name">Liam Foxcombe</p>
        <p class="person__phone">07755 618 042</p>
      </div>
      <ul class="links">
        <li>
          <svg viewBox="0 0 12 12" aria-hidden="true"><rect x="0.5" y="2" width="11" height="8" fill="var(--orange-deep)"/><path d="M0.5 2 L6 7 L11.5 2" fill="none" stroke="var(--card)" stroke-width="1"/></svg>
          operations@kmsecuritysystems.example.co.uk
        </li>
        <li>
          <svg viewBox="0 0 12 12" aria-hidden="true"><circle cx="6" cy="6" r="5.5" fill="var(--orange-deep)"/><path d="M0.5 6 H11.5 M6 0.5 C3 3.5 3 8.5 6 11.5 M6 0.5 C9 3.5 9 8.5 6 11.5" fill="none" stroke="var(--card)" stroke-width=".9"/></svg>
          www.kmsecuritysystems.example.co.uk
        </li>
      </ul>
    </div>
  </section>

  <section class="card card--back" aria-label="Card back">
    <div class="brand">
      <span class="brand__mark"></span>
      <span class="brand__name">K M Security<br>Systems</span>
    </div>
    <p class="services">Intruder Alarms<span class="dot">&bull;</span>CCTV<span class="dot">&bull;</span>Access Control</p>
  </section>
</body>
</html>
```